Packaging / Logo Design for Toddler Potty Liners

We need a packaging and logo design for a new company based in Atlanta called "WeeMeadow". We manufacture innovative, eco-friendly baby / toddler products. Our initial product is a flushable, biodegradable potty liner used for toddler potty training. We are looking for a modern / clean / eco-friendly packaging and logo design for this product. Each package will contain 20 liners. Box dimensions are as follows:

Length = 8.5in
Width = 5in
Height = 1.5in

The box will have a perforated top measuring 6.5 inches (see attached pictures). Liners will be folded inside and individually pulled out through the perforated top (similar to a Softrel box). See attached pictures of similar box.

Packaging should appeal to parents as an easy to use, eco-friendly, sanitary solution to potty training. This product is an alternative to the conventional way of cleaning / disinfecting the potty after each use, a process that most parents dread!

The closest competitors are NeatNips (www.neatnips-example.com) and Brillo (www.brillo-example.com) - you can reference their websites to get an idea for the product and use. However, their liners are not flushable and that is the biggest differentiator of this product. Their packaging seems conventional and non-inspiring so we would like our design to stand out from theirs.

We would like to see creative, modern cardboard box designs which will make our brand stand out from the competition. We would like to use one of the following color schemes: 1) a modern green color on a white background, 2) a modern green color on plain cardboard background, or 3) white on a modern green background. May use one or two additional complementary colors. See attached modern green image for inspiration. We would like to see clean lines, text and illustrations. We are looking forward to seeing any cool ideas you may have!
Updates

Brief has been updated with our desired color schemes and pictures for inspiration.  Please read updated brief before beginning your design!  Thanks so much!

Industry/Entity Type

Biodegradable

Requirements
Must have
• The front of the package should include the following info:

Logo: WeeMeadow
Product Name: Flushable Potty Chair Liners
Clean and Convenient
Fits All Potty Chairs
Sewer and Septic Safe
Patent Pending
20 Single-Use Flushable Potty Chair Liners

Package should also have space for some simple instructions (preferably with illustrations). This can be placed on one of the sides of the box.
1. Place liner over clean, dry (underline the word dry) potty bowl.
2. After your toddler uses the potty, remove liner (do not tie) and flush.
3. Give your toddler a high five!

Please submit design considering all sides of the box!

```html
<!DOCTYPE html>
<html lang="en">
<head>
<meta charset="utf-8">
<title>WeeMeadow Flushable Potty Chair Liners – Box Dieline</title>
<link rel="stylesheet" href="https://fonts.googleapis.com/css2?family=Mali:wght@600;700&display=swap">
<style>
  :root {
    --meadow-green: #a5c640;
    --ink-white: #ffffff;
    --page: #ffffff;
    --soft-line: rgba(255, 255, 255, 0.55);
  }
  html, body {
    margin: 0;
    padding: 0;
    width: 1200px;
    height: 900px;
    overflow: hidden;
    background: var(--page);
  }
  .dieline {
    display: block;
    width: 1200px;
    height: 900px;
    font-family: "Mali", "Comic Sans MS", sans-serif;
    font-weight: 700;
  }
  .box-net { fill: var(--meadow-green); }
  .ink { fill: var(--ink-white); }
  .outline { fill: none; stroke: var(--ink-white); stroke-width: 3; }
  .swirl { fill: none; stroke: var(--soft-line); stroke-width: 2; stroke-dasharray: 2 3; }
  .title-lg { font-size: 32px; }
  .title-md { font-size: 29px; }
  .title-front-top { font-size: 27px; }
  .title-sm { font-size: 25px; }
  .count { font-size: 16px; }
  .count-lg { font-size: 20px; }
  .count-sm { font-size: 9px; }
  .feature { font-size: 18px; }
  .howto { font-size: 12px; }
  .howto-head { font-size: 11.5px; }
  .brand-name { font-family: "Mali", "Comic Sans MS", sans-serif; font-weight: 700; }
  .side-copy { font-size: 7px; }
</style>
</head>
<body>
<svg class="dieline" viewBox="0 0 1200 900" xmlns="http://www.w3.org/2000/svg" role="img" aria-label="Flat dieline of the WeeMeadow flushable potty chair liner box">

  <path class="box-net" d="M333,15 H866 V330 L952,342 V410 L866,418 V423 H952 L1006,447 V713 L952,735 H866 V737 L952,745 V815 L866,828 L846,885 H353 L333,828 L247,815 V745 L333,737 V735 H247 L193,713 V447 L247,423 H333 V418 L247,410 V342 L333,330 Z"/>

  <!-- Lid panel, printed upside down -->
  <g class="lid-panel" transform="rotate(180 600 165)">
    <text class="ink count-lg" x="790" y="305" text-anchor="middle">20 Liners</text>

    <g class="how-to-use" transform="rotate(-20 695 220)">
      <ellipse class="outline" cx="695" cy="220" rx="160" ry="74"/>
      <text class="ink howto-head" x="695" y="174" text-anchor="middle">HOW TO USE...</text>
      <text class="ink howto" x="695" y="196" text-anchor="middle">1. Place liner over clean, <tspan text-decoration="underline">DRY</tspan> potty</text>
      <text class="ink howto" x="695" y="212" text-anchor="middle">bowl.</text>
      <text class="ink howto" x="695" y="231" text-anchor="middle">2. After your child uses the potty,</text>
      <text class="ink howto" x="695" y="247" text-anchor="middle">remove liner and flush.</text>
      <text class="ink howto" x="695" y="266" text-anchor="middle">3. Give your child a high five!</text>
    </g>

    <text class="ink title-lg" x="542" y="143" text-anchor="middle" textLength="410" lengthAdjust="spacingAndGlyphs" transform="rotate(-19 542 132)">Flushable Potty Chair Liners</text>

    <g class="brand" transform="translate(435 90)">
      <ellipse class="outline" rx="64" ry="54"/>
      <text class="ink brand-name" y="7" font-size="20" text-anchor="middle">WeeMeadow</text>
    </g>
  </g>

  <!-- Front panel -->
  <g class="front-panel">
    <path class="swirl" d="M430,362 C395,420 420,480 560,488 C700,495 810,470 820,420"/>

    <text class="ink title-front-top" x="538" y="390" text-anchor="middle" textLength="372" lengthAdjust="spacingAndGlyphs" transform="rotate(-5 538 380)">Flushable Potty Chair Liners</text>
    <text class="ink count" x="687" y="403" text-anchor="middle">20 Liners</text>

    <g class="brand" transform="translate(790 372)">
      <ellipse class="outline" rx="40" ry="34"/>
      <text class="ink brand-name" y="5" font-size="12" text-anchor="middle">WeeMeadow</text>
    </g>

    <g class="brand" transform="translate(425 510)">
      <ellipse class="outline" rx="82" ry="66"/>
      <text class="ink brand-name" y="8" font-size="22" text-anchor="middle">WeeMeadow</text>
    </g>

    <text class="ink title-md" x="545" y="570" text-anchor="middle" textLength="418" lengthAdjust="spacingAndGlyphs" transform="rotate(-19 545 560)">Flushable Potty Chair Liners</text>

    <g class="features">
      <ellipse class="outline" cx="702" cy="628" rx="152" ry="74" transform="rotate(-20 702 628)"/>
      <text class="ink feature" x="648" y="598" textLength="194" lengthAdjust="spacingAndGlyphs">- Clean and Convenient</text>
      <text class="ink feature" x="621" y="627" textLength="204" lengthAdjust="spacingAndGlyphs">- Sewer and Septic Safe</text>
      <text class="ink feature" x="596" y="656" textLength="194" lengthAdjust="spacingAndGlyphs">- Fits All Potty Chairs</text>
      <text class="ink feature" x="578" y="685" textLength="145" lengthAdjust="spacingAndGlyphs">- Patent Pending</text>
    </g>

    <text class="ink count-lg" x="795" y="725" text-anchor="middle">20 Liners</text>
  </g>

  <!-- Left side panel -->
  <g class="side-panel">
    <g class="brand" transform="translate(290 465)">
      <ellipse class="outline" rx="38" ry="35"/>
      <text class="ink brand-name" y="4" font-size="12" text-anchor="middle">WeeMeadow</text>
    </g>
    <text class="ink count-sm" x="290" y="512" text-anchor="middle">20 Liners</text>
    <text class="ink side-copy" text-anchor="middle" lengthAdjust="spacingAndGlyphs">
      <tspan x="290" y="531" textLength="74">Lorem ipsum dolor sit</tspan>
      <tspan x="290" y="541.5" textLength="64">amet, consectetuer</tspan>
      <tspan x="290" y="552" textLength="66">adipiscing elit, sed</tspan>
      <tspan x="290" y="562.5" textLength="66">diam nonummy nibh</tspan>
      <tspan x="290" y="573" textLength="72">euismod tincidunt ut</tspan>
      <tspan x="290" y="583.5" textLength="72">laoreet dolore magna</tspan>
      <tspan x="290" y="594" textLength="76">aliquam erat volutpat.</tspan>
      <tspan x="290" y="604.5" textLength="74">Ut wisi enim ad minim</tspan>
      <tspan x="290" y="615" textLength="68">veniam, quis nostrud</tspan>
      <tspan x="290" y="625.5" textLength="78">exerci tation ullamcor-</tspan>
      <tspan x="290" y="636" textLength="70">per suscipit lobortis</tspan>
      <tspan x="290" y="646.5" textLength="66">nisl ut aliquip ex ea</tspan>
      <tspan x="290" y="657" textLength="70">commodo consequat.</tspan>
      <tspan x="290" y="667.5" textLength="64">Duis autem vel eum</tspan>
      <tspan x="290" y="678" textLength="80">iriure dolor in hendrerit</tspan>
    </text>
  </g>

  <!-- Right side panel -->
  <g class="side-panel">
    <g class="brand" transform="translate(912 465)">
      <ellipse class="outline" rx="38" ry="35"/>
      <text class="ink brand-name" y="4" font-size="12" text-anchor="middle">WeeMeadow</text>
    </g>
    <text class="ink count-sm" x="912" y="512" text-anchor="middle">20 Liners</text>
    <text class="ink side-copy" text-anchor="middle" lengthAdjust="spacingAndGlyphs">
      <tspan x="912" y="531" textLength="74">Lorem ipsum dolor sit</tspan>
      <tspan x="912" y="541.5" textLength="64">amet, consectetuer</tspan>
      <tspan x="912" y="552" textLength="66">adipiscing elit, sed</tspan>
      <tspan x="912" y="562.5" textLength="66">diam nonummy nibh</tspan>
      <tspan x="912" y="573" textLength="72">euismod tincidunt ut</tspan>
      <tspan x="912" y="583.5" textLength="72">laoreet dolore magna</tspan>
      <tspan x="912" y="594" textLength="76">aliquam erat volutpat.</tspan>
      <tspan x="912" y="604.5" textLength="74">Ut wisi enim ad minim</tspan>
      <tspan x="912" y="615" textLength="68">veniam, quis nostrud</tspan>
      <tspan x="912" y="625.5" textLength="78">exerci tation ullamcor-</tspan>
      <tspan x="912" y="636" textLength="70">per suscipit lobortis</tspan>
      <tspan x="912" y="646.5" textLength="66">nisl ut aliquip ex ea</tspan>
      <tspan x="912" y="657" textLength="70">commodo consequat.</tspan>
      <tspan x="912" y="667.5" textLength="64">Duis autem vel eum</tspan>
      <tspan x="912" y="678" textLength="80">iriure dolor in hendrerit</tspan>
    </text>
  </g>

  <!-- Bottom panel, printed upside down -->
  <g class="bottom-panel" transform="rotate(180 600 780)">
    <g class="brand" transform="translate(810 790)">
      <ellipse class="outline" rx="32" ry="30"/>
      <text class="ink brand-name" y="4" font-size="10" text-anchor="middle">WeeMeadow</text>
    </g>
    <text class="ink count" x="695" y="808" text-anchor="middle">20 Liners</text>
    <text class="ink title-sm" x="552" y="781" text-anchor="middle" textLength="372" lengthAdjust="spacingAndGlyphs" transform="rotate(-4 552 772)">Flushable Potty Chair Liners</text>
  </g>
</svg>
</body>
</html>
```